School teacher strategies for teachers to improve their lessons.

This is for displays for teachers in their office about how to best teach students. This should be styled in a professional way that aligns with the colour themes of the school.

For reference, here is the school's website:
https://talvingrovehs.norvale-learn.edu.au/

I have attached a previous document "Steady Practices" - please use similar theme.

Target Market(s)

teachers at this school

Colors

Requirements
Must have
• School logo. And aligned to previous designs

```html
<!DOCTYPE html>
<html lang="en">
<head>
<meta charset="utf-8">
<title>Talvin Grove Instructional Model – Learning Goals &amp; Success Criteria</title>
<link rel="stylesheet" href="https://fonts.googleapis.com/css2?family=Outfit:wght@300;400;500;600;700&display=swap">
<style>
  :root {
    --navy: #0e3f82;
    --title-blue: #164c99;
    --ink: #1b1b1f;
    --body: #2c2c33;
    --band-yellow: #f8ea7c;
    --accent-yellow: #f6e64b;
    --bulb-yellow: #f7dd5a;
    --cream: #fdfcf3;
    --road-pale: #eef2f9;
    --road-soft: #d6e0f0;
    --white: #ffffff;
  }
  * { margin: 0; padding: 0; box-sizing: border-box; }
  html, body { width: 911px; height: 1200px; overflow: hidden; background: var(--white); }
  body { font-family: "Outfit", sans-serif; color: var(--ink); position: relative; }

  .brand { position: absolute; left: 62px; top: 74px; width: 100px; display: flex; flex-direction: column; align-items: center; gap: 8px; }
  .brand-square { width: 46px; height: 46px; background: var(--navy); }
  .brand-name { font-weight: 700; font-size: 15px; color: var(--navy); text-align: center; line-height: 1.1; }

  .title { position: absolute; left: 186px; top: 80px; }
  .title-main { font-weight: 700; font-size: 33px; letter-spacing: -0.6px; color: var(--title-blue); line-height: 1.05; }
  .title-sub { font-weight: 400; font-size: 40px; letter-spacing: -0.6px; color: var(--ink); line-height: 1.15; margin-top: 2px; }

  .intro-band { position: absolute; left: 64px; top: 192px; width: 770px; height: 86px; background: var(--band-yellow); padding: 13px 0 0 20px; font-size: 21.5px; line-height: 1.22; color: var(--ink); font-weight: 400; }
  .intro-band strong { font-weight: 600; }
  .bulb-art { position: absolute; left: 762px; top: 176px; width: 74px; height: 124px; border-radius: 37px 37px 14px 14px; background: radial-gradient(circle at 50% 35%, #fff6b0 0%, #f9c531 45%, #e38a14 80%, #8a8a8a 100%); }

  .examples { position: absolute; left: 64px; top: 304px; width: 740px; list-style: none; }
  .examples li { position: relative; padding-left: 21px; font-size: 16.5px; font-weight: 300; line-height: 1.3; color: var(--body); margin-bottom: 20px; }
  .examples li::before { content: ""; position: absolute; left: 0; top: 5px; border-left: 9px solid var(--navy); border-top: 5px solid transparent; border-bottom: 5px solid transparent; }

  .checklist { position: absolute; left: 65px; top: 430px; width: 783px; height: 280px; background: var(--navy); border-radius: 3px; padding: 18px 22px 0 21px; }
  .checklist h2 { font-weight: 600; font-size: 26px; color: var(--accent-yellow); letter-spacing: -0.3px; line-height: 1; }
  .checklist-cols { display: flex; margin-top: 20px; }
  .checklist-col { list-style: none; }
  .checklist-col.left { width: 386px; padding-right: 22px; }
  .checklist-col.right { width: 340px; }
  .checklist-col li { position: relative; padding-left: 27px; font-size: 16.5px; font-weight: 300; line-height: 21px; color: var(--white); margin-bottom: 9px; }
  .checklist-col li b { font-weight: 500; color: var(--accent-yellow); }
  .checklist-col li svg { position: absolute; left: 0; top: 3px; width: 14px; height: 14px; }

  .wwh h3 { font-weight: 600; font-size: 20px; color: var(--ink); letter-spacing: -0.2px; }
  .wwh ul { list-style: none; margin-top: 13px; }
  .wwh li { position: relative; padding-left: 22px; font-size: 14.5px; font-weight: 300; line-height: 20px; color: var(--body); margin-bottom: 1px; }
  .wwh li b { font-weight: 500; color: var(--ink); }
  .wwh li svg { position: absolute; left: 0; top: 3px; width: 10px; height: 14px; }
  .curriculum { position: absolute; left: 65px; top: 753px; width: 362px; }
  .behaviour-panel { position: absolute; left: 456px; top: 742px; width: 389px; height: 219px; background: var(--cream); }
  .behaviour { position: absolute; left: 478px; top: 753px; width: 332px; }

  .road-art { position: absolute; left: 0; top: 985px; width: 520px; height: 190px; background: linear-gradient(160deg, var(--road-pale) 0%, var(--road-soft) 100%); }
  .road-label { position: absolute; font-size: 14px; font-weight: 300; color: var(--ink); line-height: 18px; }

  .target-art { position: absolute; left: 527px; top: 944px; width: 92px; height: 92px; border-radius: 50%; background: radial-gradient(circle, #f4c426 0%, #fbe67a 30%, #f4c01e 55%, #e2a10d 100%); }

  .closing { position: absolute; left: 525px; top: 1032px; font-weight: 700; font-size: 46px; line-height: 52px; color: var(--title-blue); letter-spacing: -0.8px; }
</style>
</head>
<body>

  <div class="brand">
    <div class="brand-square"></div>
    <div class="brand-name">Talvin Grove</div>
  </div>

  <header class="title">
    <h1 class="title-main">TALVIN GROVE INSTRUCTIONAL MODEL</h1>
    <p class="title-sub">Learning Goals &amp; Success Criteria</p>
  </header>

  <div class="intro-band">
    A guide for teachers to craft clear learning goals &amp;<br>
    success criteria aligned to <strong>How Talvin Grove Students Learn.</strong>
  </div>
  <div class="bulb-art" role="img" aria-label="Illustration of a glowing light bulb"></div>

  <ul class="examples">
    <li>By the end of the lesson, students will apply Pythagoras’ theorem to find the hypotenuse of a right triangle with integer side lengths.</li>
    <li>By the end of the lesson, students will describe two factors that influence liveability in their local area using evidence from a map.</li>
  </ul>

  <section class="checklist">
    <h2>Essentials Checklist</h2>
    <div class="checklist-cols">
      <ul class="checklist-col left">
        <li><svg viewBox="0 0 14 14"><path d="M8 1.5H1.5v11h11V6" fill="none" stroke="#f6e64b" stroke-width="1.5"/><path d="M4.5 6.5l2.5 2.5L13 2.5" fill="none" stroke="#f6e64b" stroke-width="1.5"/></svg><b>About learning, not tasks:</b> focus on knowledge/skill students will learn today.</li>
        <li><svg viewBox="0 0 14 14"><path d="M8 1.5H1.5v11h11V6" fill="none" stroke="#f6e64b" stroke-width="1.5"/><path d="M4.5 6.5l2.5 2.5L13 2.5" fill="none" stroke="#f6e64b" stroke-width="1.5"/></svg><b>Right verb, right level:</b> choose a precise Bloom’s/cognitive verb.</li>
        <li><svg viewBox="0 0 14 14"><path d="M8 1.5H1.5v11h11V6" fill="none" stroke="#f6e64b" stroke-width="1.5"/><path d="M4.5 6.5l2.5 2.5L13 2.5" fill="none" stroke="#f6e64b" stroke-width="1.5"/></svg><b>One idea only:</b> keep scope tight to manage cognitive load.</li>
        <li><svg viewBox="0 0 14 14"><path d="M8 1.5H1.5v11h11V6" fill="none" stroke="#f6e64b" stroke-width="1.5"/><path d="M4.5 6.5l2.5 2.5L13 2.5" fill="none" stroke="#f6e64b" stroke-width="1.5"/></svg><b>Student friendly:</b> plain language students can restate; accessible to all students.</li>
      </ul>
      <ul class="checklist-col right">
        <li><svg viewBox="0 0 14 14"><path d="M8 1.5H1.5v11h11V6" fill="none" stroke="#f6e64b" stroke-width="1.5"/><path d="M4.5 6.5l2.5 2.5L13 2.5" fill="none" stroke="#f6e64b" stroke-width="1.5"/></svg><b>Visible &amp; revisited:</b> display it; say it at transitions and again during the review at lesson end.</li>
        <li><svg viewBox="0 0 14 14"><path d="M8 1.5H1.5v11h11V6" fill="none" stroke="#f6e64b" stroke-width="1.5"/><path d="M4.5 6.5l2.5 2.5L13 2.5" fill="none" stroke="#f6e64b" stroke-width="1.5"/></svg><b>Assessable:</b> design quick checks and an exit slip that align to the Success Criteria.</li>
        <li><svg viewBox="0 0 14 14"><path d="M8 1.5H1.5v11h11V6" fill="none" stroke="#f6e64b" stroke-width="1.5"/><path d="M4.5 6.5l2.5 2.5L13 2.5" fill="none" stroke="#f6e64b" stroke-width="1.5"/></svg><b>Same Learning Goal for all:</b> differentiate supports (scaffolds/groups), not the intention.</li>
      </ul>
    </div>
  </section>

  <section class="wwh curriculum">
    <h3>Curriculum (What / How / Why)</h3>
    <ul>
      <li><svg viewBox="0 0 10 14"><circle cx="5" cy="5" r="4.5" fill="#f7dd5a"/><rect x="3" y="10" width="4" height="3" rx="1" fill="#f7dd5a"/></svg><b>What:</b> the specific knowledge/skill linked to today’s learning goal.</li>
      <li><svg viewBox="0 0 10 14"><circle cx="5" cy="5" r="4.5" fill="#f7dd5a"/><rect x="3" y="10" width="4" height="3" rx="1" fill="#f7dd5a"/></svg><b>How:</b> the routine/strategy students will use to demonstrate it (e.g., worked example steps, analysis routine, calculation method).</li>
      <li><svg viewBox="0 0 10 14"><circle cx="5" cy="5" r="4.5" fill="#f7dd5a"/><rect x="3" y="10" width="4" height="3" rx="1" fill="#f7dd5a"/></svg><b>Why:</b> the purpose or connection (e.g., links to the next lesson/assessment; helps solve real problems).</li>
    </ul>
  </section>

  <div class="behaviour-panel"></div>
  <section class="wwh behaviour">
    <h3>Behaviour (What / How / Why)</h3>
    <ul>
      <li><svg viewBox="0 0 10 14"><circle cx="5" cy="5" r="4.5" fill="#f7dd5a"/><rect x="3" y="10" width="4" height="3" rx="1" fill="#f7dd5a"/></svg><b>What:</b> the explicit behaviour expectation (e.g., track the speaker; voice level; hands/signals).</li>
      <li><svg viewBox="0 0 10 14"><circle cx="5" cy="5" r="4.5" fill="#f7dd5a"/><rect x="3" y="10" width="4" height="3" rx="1" fill="#f7dd5a"/></svg><b>How:</b> the routine to meet it (e.g., attention signal → pause → response; partner roles; “<b>Ask 3 before me</b>”).</li>
      <li><svg viewBox="0 0 10 14"><circle cx="5" cy="5" r="4.5" fill="#f7dd5a"/><rect x="3" y="10" width="4" height="3" rx="1" fill="#f7dd5a"/></svg><b>Why:</b> maximises learning time, safety, and fairness for everyone.</li>
    </ul>
  </section>

  <div class="road-art" role="img" aria-label="Illustration of a winding navy road leading to the target, with stops for each lesson phase"></div>
  <span class="road-label" style="left:74px; top:1057px;">Warm up</span>
  <span class="road-label" style="left:182px; top:1090px;">I Do</span>
  <span class="road-label" style="left:200px; top:1003px;">We Do</span>
  <span class="road-label" style="left:352px; top:1032px;">You Do</span>
  <span class="road-label" style="left:349px; top:1115px;">You Do<br>Together</span>
  <span class="road-label" style="left:397px; top:959px;">Review</span>

  <div class="target-art" role="img" aria-label="Illustration of a yellow target with a dart in the bullseye"></div>

  <div class="closing">Learning Goal<br>&amp; Success</div>

</body>
</html>
```